Quill Yard Profile Banner Needed

I am in need of a Quill Yard Banner photo for my profile. The dimensions are 1584 x 396 pixels and the bottom left is where Quill Yard places my photo over so be aware of that. I attached an example for your reference.

I have also attached my logo and business card so you can keep the same color & style conistant.

Also add the following text:

"Preserve capital with a tax advantaged lease for equipment, vehicles, software and more! $5,000 - $50m"

You can also look at our website here:
www.HarborBrookFunding.example

```html
<!DOCTYPE html>
<html lang="en">
<head>
<meta charset="utf-8">
<title>Harbor Brook Funding – Quill Yard Profile Banner</title>
<link href="https://fonts.googleapis.com/css2?family=Alegreya:ital,wght@0,400;1,400&display=swap" rel="stylesheet">
<style>
  :root {
    --page-bg: #ffffff;
    --band-bg: #383446;
    --text-light: #ffffff;
  }
  html, body {
    margin: 0;
    padding: 0;
    width: 1200px;
    height: 433px;
    overflow: hidden;
    background: var(--page-bg);
  }
  .canvas {
    position: relative;
    width: 1200px;
    height: 433px;
  }
  .banner {
    position: absolute;
    left: 44px;
    top: 108px;
    width: 1112px;
    height: 191px;
    background: var(--band-bg);
  }
  .brand-name {
    position: absolute;
    left: 0;
    right: 0;
    top: 36px;
    margin: 0;
    text-align: center;
    font-family: "Alegreya", Georgia, serif;
    font-weight: 400;
    font-size: 36px;
    letter-spacing: 1.5px;
    line-height: 1;
    color: var(--text-light);
    text-transform: uppercase;
  }
  .tagline {
    position: absolute;
    left: 0;
    right: 0;
    top: 120px;
    margin: 0;
    text-align: center;
    font-family: "Alegreya", Georgia, serif;
    font-style: italic;
    font-weight: 400;
    font-size: 22px;
    line-height: 27px;
    color: var(--text-light);
  }
</style>
</head>
<body>
  <main class="canvas">
    <section class="banner">
      <h1 class="brand-name">Harbor Brook Funding</h1>
      <p class="tagline">Preserve capital with a tax advantaged lease for equipment,<br>vehicles, software and more! $5,000 - $50m</p>
    </section>
  </main>
</body>
</html>
```